Newsletter-Design für Online-Versandhandel
Zielgruppe
Wir sind ein online Versand Handel mit dem Schwerpunkt auf Bio Bettwaren. Unsere Zielgruppe sind ökologisch bewusste Menschen mittleren bis höheren Alters.
Aufgabenstellung
Unsere Corporate Farbe ist vornehmlich ein sanftes Grün.
www.bettwelt-lindqvar.example
Hier eine Auswahl von Newslettern
http://newsletter.waldmoos-shop.example/u/gm.php?prm=4pTrKmZyyQ_815204736_5390418_23847
http://newslink.lodenfalt.example/u/gm.php?prm=bRx72kdfQ_962157384_3047215_81530
Bisher haben wir unsere NL als kleinen, persönlichen Text gestaltet und dazu zwei oder drei Teaser.
Den Text möchte ich beibehalten und neben meiner Unterschrift ein ein kleines persönliches Bild einfügen.
Wichtig! Wir versenden mit postfink, wir benötigen eine dafür kompatible Vorlage.

```html
<!DOCTYPE html>
<html lang="de">
<head>
<meta charset="utf-8">
<title>Lindqvar Naturversand – Newsletter</title>
<link href="https://fonts.googleapis.com/css2?family=Ubuntu:ital,wght@0,300;0,400;0,500;0,700;1,700&display=swap" rel="stylesheet">
<style>
:root{
  --bg-top:#5a7db5;
  --bg-bottom:#b9d3f2;
  --green:#0a9444;
  --green-dark:#077235;
  --green-text:#0b9a3c;
  --ink:#333333;
  --ink-soft:#444444;
  --white:#ffffff;
  --shadow:#3b3b3b;
}
*{box-sizing:border-box;margin:0;padding:0}
html,body{width:800px;height:1200px;overflow:hidden}
body{
  font-family:"Ubuntu",sans-serif;color:var(--ink);
  background:linear-gradient(var(--bg-top),var(--bg-bottom) 60%,#c3dbf6);
  position:relative;
}
.preheader{position:absolute;top:13px;width:100%;text-align:center;font-size:9.5px;color:#e8eefa;letter-spacing:.1px}
.card{position:absolute;left:16px;top:40px;width:768px;height:1080px;background:var(--white);border-radius:10px;overflow:hidden}
.brand{position:absolute;left:26px;top:24px;display:flex;align-items:center;gap:10px}
.brand-mark{width:34px;height:34px;border-radius:50%;background:var(--green)}
.brand-name{font-size:30px;font-weight:700;color:var(--green)}
.brand-sub{position:absolute;left:26px;top:66px;font-size:10.5px;color:var(--green-text)}
.header-note{position:absolute;right:26px;top:56px;text-align:right;font-size:9.8px;line-height:13px;color:var(--ink)}
.header-note .accent{color:var(--green-text)}
.nav{position:absolute;top:104px;left:0;width:100%;display:flex;justify-content:center;gap:27px;font-size:11px;font-weight:500;color:#3a3a3a}
.welcome{position:absolute;top:148px;width:100%;text-align:center;font-size:15.5px;font-weight:700;color:var(--green-text)}
.intro{position:absolute;top:182px;left:64px;width:640px;text-align:center;font-size:10.4px;line-height:14.4px;color:var(--ink-soft);white-space:nowrap}
.coupon{position:absolute;left:102px;top:259px;width:568px;height:74px;border-radius:8px;background:var(--green);box-shadow:0 3px 0 var(--shadow);text-align:center;color:var(--white)}
.coupon-label{display:block;margin-top:18px;font-size:12.5px;font-weight:300;color:#a8dbb9}
.coupon-code{display:block;font-size:29px;font-weight:300;letter-spacing:.5px;line-height:30px}
.hero{position:absolute;left:0;top:372px;width:768px;height:314px}
.hero-photo{position:absolute;inset:0;background:linear-gradient(90deg,#9bc27a 0%,#e6e3ea 35%,#f3f1f4 60%,#ffffff 100%)}
.hero-badge{position:absolute;left:28px;top:123px;width:148px;height:148px;border-radius:50%;background:var(--green);border:3px solid var(--white);color:var(--white);text-align:center;padding-top:53px}
.hero-badge small{display:block;font-size:12.5px;font-weight:300}
.hero-badge strong{display:block;font-size:19px;font-weight:700}
.hero-copy{position:absolute;left:371px;top:64px;width:300px;font-size:10.4px;line-height:14.4px;color:var(--ink)}
.hero-copy h2{font-size:15px;font-style:italic;font-weight:700;color:#3a3a3a;margin-bottom:4px;white-space:nowrap}
.btn{display:block;height:27px;border-radius:3px;background:var(--green);box-shadow:0 2px 0 var(--shadow);color:var(--white);font-size:11px;text-align:center;line-height:28px}
.hero .btn{position:absolute;left:371px;top:253px;width:158px}
.products{position:absolute;top:712px;left:26px;width:716px;display:flex;justify-content:space-between}
.product{position:relative;width:204px;height:330px;text-align:center}
.product-photo{position:absolute;top:26px;left:0;width:204px;height:206px;background:linear-gradient(#efe9dc,#e3dac7 55%,#ffffff)}
.neu{position:absolute;top:8px;left:69px;width:66px;height:66px;transform:rotate(45deg);background:var(--green-dark);box-shadow:0 0 0 3px rgba(255,255,255,.6)}
.neu-label{position:absolute;top:29px;left:0;width:100%;font-size:19px;font-weight:500;color:var(--white);line-height:24px}
.product-text{position:absolute;top:210px;left:0;width:100%;font-size:10.8px;line-height:16px;color:var(--ink-soft)}
.product-text b{font-weight:500;color:#222}
.product .btn{position:absolute;top:294px;left:23px;width:158px}
.footer{position:absolute;top:1133px;left:42px;width:716px;font-size:9.5px;line-height:11.4px;color:#2a2a2a}
.footer-left{position:absolute;left:0;top:0}
.footer-right{position:absolute;right:0;top:0;text-align:right}
.social{position:absolute;left:306px;top:14px;display:flex;gap:3px}
.social span{width:32px;height:32px;background:#3e5d87}
</style>
</head>
<body>
<div class="preheader">NEWSLETTER WIRD NICHT RICHTIG ANGEZEIGT? HIER KLICKEN.</div>

<main class="card">
  <div class="brand"><span class="brand-mark"></span><span class="brand-name">Lindqvar</span></div>
  <div class="brand-sub">Seit 25 Jahren ökologisches Versandhaus</div>
  <div class="header-note"><span class="accent">BITTE FÜGEN SIE UNS IHREM ADRESSBUCH HINZU</span><br>INNERHALB DEUTSCHLANDS VERSENDEN WIR PORTOFREI</div>

  <nav class="nav"><span>HOME</span><span>SCHLAFEN</span><span>HANDWEBTEPPICHE</span><span>EDELSTEIN-SCHMUCK</span><span>WÄRMEAUFLAGE</span><span>ALLERGIKERPRODUKTE</span></nav>

  <h1 class="welcome">Herzlich Willkommen bei Lindqvar Naturversand!</h1>
  <p class="intro">Kaufen Sie bei uns hochwertige, ökologische Produkte für natürliches Wohnen und gesundes Schlafen.<br>Bei uns finden Sie Oberbetten, Handwebteppiche, Produkte zum Schutz vor Elektrosmog, orthopädische Kissen,<br>Allergiker Bettdecken, Kirschkernkissen, Nackenwärmer, Daunenkissen, Kaschmirdecken.<br>Liegen Sie gesund und richtig in unseren Massivholzbetten, auf unseren Naturlatexmatratzen und unseren Bio<br>Lattenrosten. Kuscheln Sie sich in unsere ökologischen Bettwaren aus kbA Baumwolle mit den verschiedensten ....</p>

  <div class="coupon"><span class="coupon-label">COUPONCODE:</span><span class="coupon-code">PORTOFREI2018</span></div>

  <section class="hero">
    <div class="hero-photo" role="img" aria-label="Foto: Mädchen liegt auf einer Matratze in einer Frühlingswiese mit Gänseblümchen"></div>
    <div class="hero-badge"><small>FRÜHLING FÜR</small><strong>ALLERGIKER</strong></div>
    <div class="hero-copy">
      <h2>FRÜHLING &amp; SOMMER FÜR ALLERGIKER</h2>
      <p>Wie kann eine allergische Reaktion vermieden werden?<br>Matratzen, die älter als acht Jahre sind, sollten<br>ausgetauscht werden.<br>Spezielle allergiedichte Überzüge für Matratzen,<br>Kopfkissen und Überbetten sollten zur Verwendung<br>kommen. Sowohl Matratzen-, Kissen- und Bettbezüge, als<br>auch Steppbetten sollten bei 60° - 95°C gewaschen werden.<br><br>Wir empfehlen Ihnen folgende Füllmaterialien:<br>&nbsp;- Baumwolle mit medivera-Ausrüstung<br>&nbsp;- Maisvlies</p>
    </div>
    <span class="btn">MEHR INFORMATION</span>
  </section>

  <section class="products">
    <article class="product">
      <div class="product-photo" role="img" aria-label="Foto: Matratzenauflage mit Eckgummi"></div>
      <span class="neu"></span><span class="neu-label">NEU</span>
      <p class="product-text"><b>"MATRATZENAUFLAGE"</b><br>Die Matratzenauflage schützt<br>Ihre wertvolle Matratze<br>und besitzt ...</p>
      <span class="btn">MEHR INFORMATION</span>
    </article>
    <article class="product">
      <div class="product-photo" role="img" aria-label="Foto: Matratzenauflage mit Eckgummi"></div>
      <span class="neu"></span><span class="neu-label">NEU</span>
      <p class="product-text"><b>"MATRATZENAUFLAGE"</b><br>Die Matratzenauflage schützt<br>Ihre wertvolle Matratze<br>und besitzt ...</p>
      <span class="btn">MEHR INFORMATION</span>
    </article>
    <article class="product">
      <div class="product-photo" role="img" aria-label="Foto: Matratzenauflage mit Eckgummi"></div>
      <span class="neu"></span><span class="neu-label">NEU</span>
      <p class="product-text"><b>"MATRATZENAUFLAGE"</b><br>Die Matratzenauflage schützt<br>Ihre wertvolle Matratze<br>und besitzt ...</p>
      <span class="btn">MEHR INFORMATION</span>
    </article>
  </section>
</main>

<footer class="footer">
  <div class="footer-left">NATUR-VERSAND<br>LINDQVAR GMBH<br><br>AUENWEG 12<br>79999 MUSTERBACH</div>
  <div class="social" aria-label="Soziale Netzwerke"><span></span><span></span><span></span></div>
  <div class="footer-right">Kontakt:<br>Zentrale: 07000 555 0100<br>Fax: 07000 555 0199<br>Internet: www.bettwelt-lindqvar.example<br>EMail: info@bettwelt-lindqvar.example</div>
</footer>
</body>
</html>
```